Duel Business card

Want an edgy business card that shows both of our companies on each side of the card, OR both together with a cool design.

*Must be edgy: We have attached our two business logos. We are a bail bond and immigration bond company.

Would like the address on one side only.
Need Phone, cell, website, address, and Name

Company Name 1: Cellgate Release Partners
www.cellgatereleasepartners.example

Company Name 2: Borderline Surety Associates
www.borderlinesuretyassociates.example

These cards will need to be easily changeable so I can modify new employees

Target Market(s)

people in jail, takign imigrants out of jail and from being taken back to there country

Industry/Entity Type

Business

Requirements
Must have
• Include both logos attached

```html
<!DOCTYPE html>
<html lang="en">
<head>
<meta charset="utf-8">
<title>Cellgate Release Partners &amp; Borderline Surety Associates – Business Card</title>
<link rel="stylesheet" href="https://fonts.googleapis.com/css2?family=Jost:wght@400;500;700&display=swap">
<style>
  :root {
    --stage: #8a8a86;
    --navy: #1b3d6e;
    --royal: #1d3f96;
    --ink: #1c3a8a;
    --paper: #f4f5f7;
    --white: #ffffff;
    --badge: #e6e8ec;
  }
  * { box-sizing: border-box; margin: 0; padding: 0; }
  html, body {
    width: 1200px; height: 792px; overflow: hidden;
    background: var(--stage);
    font-family: "Jost", sans-serif;
  }
  .stage { position: relative; width: 1200px; height: 792px; }
  .card {
    position: absolute; top: 241px;
    width: 540px; height: 309px;
    overflow: hidden; border-radius: 3px;
    box-shadow: 0 10px 28px rgba(0,0,0,.28);
  }
  .card--front { left: 40px; display: flex; }
  .card--back { left: 620px; display: flex; background: var(--paper); }

  /* front */
  .front-panel { position: relative; width: 50%; height: 100%; display: flex; flex-direction: column; align-items: center; justify-content: center; color: var(--white); }
  .front-panel--surety { background: var(--navy); }
  .front-panel--release { background: var(--royal); border-left: 3px solid var(--white); }
  .star-field { position: absolute; inset: 0; background: linear-gradient(135deg, #1f4478, #183866); }
  .brand-mark { position: relative; width: 52px; height: 52px; border-radius: 50%; background: var(--badge); margin-bottom: 14px; }
  .brand-mark--gold { background: #e0b638; }
  .brand-name { position: relative; text-align: center; font-weight: 700; text-transform: uppercase; line-height: 1.1; letter-spacing: .5px; }
  .brand-name--surety { font-size: 22px; color: var(--white); width: 200px; }
  .brand-name--release { font-size: 24px; color: var(--white); width: 220px; }
  .site { position: absolute; bottom: 16px; left: 0; right: 0; text-align: center; font-size: 11px; font-weight: 400; letter-spacing: .3px; color: var(--white); }

  /* back */
  .back-strip { width: 30%; height: 100%; background: var(--royal); display: flex; flex-direction: column; align-items: center; justify-content: center; color: var(--white); padding: 0 10px; }
  .back-strip .brand-mark { width: 36px; height: 36px; margin-bottom: 10px; }
  .brand-name--small { font-size: 12px; width: 130px; }
  .back-details { position: relative; width: 70%; padding: 34px 30px 0 26px; color: var(--ink); }
  .holder-name { font-size: 24px; font-weight: 400; letter-spacing: .5px; line-height: 1; }
  .holder-role { display: flex; align-items: flex-end; gap: 8px; font-size: 13px; margin-top: 2px; }
  .holder-role::after { content: ""; flex: 1; border-bottom: 1.5px solid var(--ink); margin-bottom: 3px; }
  .contact { margin-top: 46px; display: grid; grid-template-columns: 64px 1fr; row-gap: 6px; font-size: 14px; line-height: 1.25; }
  .contact dt { font-weight: 400; }
  .contact dd::before { content: ": "; }
  .contact .address-line2 { display: block; padding-left: 8px; }
</style>
</head>
<body>
<main class="stage">
  <section class="card card--front" aria-label="Business card front">
    <div class="front-panel front-panel--surety">
      <div class="star-field" role="img" aria-label="Faint star pattern on navy background"></div>
      <span class="brand-mark" aria-hidden="true"></span>
      <p class="brand-name brand-name--surety">Borderline Surety Associates</p>
      <p class="site">www.borderlinesuretyassociates.example</p>
    </div>
    <div class="front-panel front-panel--release">
      <span class="brand-mark brand-mark--gold" aria-hidden="true"></span>
      <p class="brand-name brand-name--release">Cellgate Release Partners</p>
      <p class="site">www.cellgatereleasepartners.example</p>
    </div>
  </section>

  <section class="card card--back" aria-label="Business card back">
    <div class="back-strip">
      <span class="brand-mark" aria-hidden="true"></span>
      <p class="brand-name brand-name--small">Borderline Surety Associates</p>
    </div>
    <div class="back-details">
      <h1 class="holder-name">JORDAN AVERY</h1>
      <p class="holder-role">manager</p>
      <dl class="contact">
        <dt>Phone</dt><dd>+00 123 456 789</dd>
        <dt>Cell</dt><dd>+00 123 456 789</dd>
        <dt>Address</dt><dd>Your Address Goes Here<span class="address-line2">City, Country, Zipcode</span></dd>
      </dl>
    </div>
  </section>
</main>
</body>
</html>
```